Tolliver Business Services Stationary
Letterhead, Business Card, Envelope
Tolliver Business Services Stationary -
Creative Brief
Simple
Dale Pruett
Bookkeeping and Tax Preparation
PO Box 4713 Seattle, WA 98109
dpruettpruett@tolliverllc.example
www.tolliverllc.example
The info for the business card is fake because this is not a private contest. I will provide the correct info when I finalize the contest. I need a standard sized business card, letterhead, and envelope. Finished artwork needs to be vector format. I have attached designs that I like and my company logo.
Maybe just the logo? reversed colors? I've attached samples and layouts the I like.

```html
<!DOCTYPE html>
<html lang="en">
<head>
<meta charset="utf-8">
<title>Tolliver Business Services Stationery</title>
<link href="https://fonts.googleapis.com/css2?family=EB+Garamond:wght@400;500&family=Arimo:wght@400&display=swap" rel="stylesheet">
<style>
  :root {
    --bg: #e4e4e4;
    --paper: #ffffff;
    --ink: #2a2a2a;
    --ink-soft: #555555;
    --ink-faint: #7a7a7a;
    --mark: #2b2b2b;
    --dark-1: #5c5c5c;
    --dark-2: #262626;
    --band-1: #f2f2f2;
    --band-2: #a9a9a9;
    --tab: #5a5a5a;
    --tab-text: #d8d8d8;
  }
  * { box-sizing: border-box; margin: 0; padding: 0; }
  html, body { width: 1200px; height: 732px; overflow: hidden; }
  body {
    background: var(--bg);
    font-family: "EB Garamond", "Times New Roman", serif;
    color: var(--ink);
    position: relative;
  }
  .sheet {
    position: absolute;
    background: var(--paper);
    box-shadow: 0 2px 6px rgba(0,0,0,.22);
    overflow: hidden;
  }

  /* brand lockup */
  .brand { display: flex; align-items: center; gap: 8px; }
  .brand-square { width: 20px; height: 20px; background: var(--mark); flex: none; }
  .brand-text { line-height: 1; }
  .brand-name {
    font-size: 28px; font-weight: 400; color: var(--mark);
    text-transform: uppercase; letter-spacing: 1px;
  }
  .brand-sub {
    font-size: 7px; letter-spacing: 2px; text-transform: uppercase;
    color: var(--mark); margin-top: 2px;
  }

  /* letterhead */
  .letterhead { left: 5px; top: 5px; width: 566px; height: 722px; }
  .letterhead .brand { position: absolute; left: 46px; top: 26px; }
  .letterhead .contact {
    position: absolute; left: 74px; top: 90px;
    font-size: 8.5px; line-height: 11px; color: var(--ink-soft);
  }
  .letter-body {
    position: absolute; left: 46px; top: 212px; width: 474px;
    font-size: 9.5px; line-height: 13.5px; color: var(--ink-soft);
    text-align: justify;
  }
  .letter-body p { margin-bottom: 14px; }
  .letter-closing {
    position: absolute; left: 46px; top: 634px;
    font-size: 9.5px; line-height: 13px; color: var(--ink-soft);
  }
  .letter-closing .signer { margin-top: 22px; }
  .letter-band {
    position: absolute; left: 0; bottom: 0; width: 100%; height: 36px;
    background: linear-gradient(180deg, var(--band-1), var(--band-2));
  }
  .letter-band .brand-square {
    position: absolute; right: 34px; top: 8px; width: 20px; height: 20px;
  }

  /* business card */
  .card-front { left: 595px; top: 7px; width: 257px; height: 151px; text-align: center; }
  .card-front .brand { position: absolute; left: 66px; top: 14px; gap: 6px; }
  .card-front .brand-square { width: 13px; height: 13px; }
  .card-front .brand-name { font-size: 19px; }
  .card-front .brand-sub { font-size: 5px; letter-spacing: 1.5px; }
  .card-details {
    position: absolute; left: 0; right: 0; top: 58px;
    font-size: 6.5px; line-height: 9px; color: var(--ink-soft);
  }
  .card-details .person { font-size: 8px; color: var(--ink); letter-spacing: .5px; }
  .card-details .role { margin-bottom: 5px; }
  .card-back {
    left: 864px; top: 7px; width: 195px; height: 151px;
    background: linear-gradient(135deg, var(--dark-1), var(--dark-2));
    display: flex; align-items: center; justify-content: center;
  }
  .card-back .brand-square { background: #e8e8e8; width: 16px; height: 16px; }
  .card-back .brand-name { color: #e8e8e8; font-size: 22px; }

  /* envelope */
  .envelope-front { left: 595px; top: 178px; width: 464px; height: 200px; }
  .envelope-front .brand { position: absolute; left: 34px; top: 30px; }
  .envelope-front .contact {
    position: absolute; left: 62px; top: 78px;
    font-size: 7.5px; line-height: 10px; color: var(--ink-soft);
  }
  .envelope-back { left: 595px; top: 390px; width: 464px; height: 335px; }
  .envelope-back svg { position: absolute; left: 0; top: 0; }

  /* presentation tab */
  .package-tab {
    position: absolute; left: 1082px; top: 0; width: 114px; height: 258px;
    background: var(--tab); border-radius: 0 0 6px 6px;
    display: flex; align-items: center; justify-content: center;
  }
  .package-tab span {
    font-family: "Arimo", Arial, sans-serif; font-size: 22px; color: var(--tab-text);
    transform: rotate(-90deg); white-space: nowrap;
  }
</style>
</head>
<body>

<section class="sheet letterhead">
  <div class="brand">
    <div class="brand-square"></div>
    <div class="brand-text">
      <div class="brand-name">Tolliver</div>
      <div class="brand-sub">Business Services</div>
    </div>
  </div>
  <div class="contact">
    PO Box 4713 Seattle, WA 98109<br>
    Phone (206) 555-0142<br>
    Fax (206) 555-0143<br>
    www.tolliverllc.example
  </div>
  <div class="letter-body">
    <p>Dear client, thank you for choosing our office for your bookkeeping and tax preparation needs this season. We have reviewed the documents you sent and prepared a short summary of the items that still require your attention before we can complete the return. Please read the notes below and contact us with any questions.</p>
    <p>Our records show that several monthly statements are missing from the second quarter. Once these are received we will reconcile the accounts, update the ledger and send you a final report for review. We also recommend setting aside copies of all receipts related to equipment purchases, travel and office rent, as these may qualify for deductions this year.</p>
    <p>Please note that our office hours will change during the filing period. We will be open six days a week from early March through the middle of April, and appointments can be scheduled by phone or email. We look forward to working with you again and thank you for your continued trust in our services.</p>
  </div>
  <div class="letter-closing">
    <div>Best Regards,</div>
    <div class="signer">Dale Pruett</div>
  </div>
  <div class="letter-band"><div class="brand-square"></div></div>
</section>

<section class="sheet card-front">
  <div class="brand">
    <div class="brand-square"></div>
    <div class="brand-text">
      <div class="brand-name">Tolliver</div>
      <div class="brand-sub">Business Services</div>
    </div>
  </div>
  <div class="card-details">
    <div class="person">Dale Pruett</div>
    <div class="role">Bookkeeping and Tax Preparation</div>
    <div>PO Box 4713 Seattle, WA 98109</div>
    <div>Phone (206) 555-0142</div>
    <div>Fax (206) 555-0143</div>
    <div>dpruettpruett@tolliverllc.example</div>
    <div>www.tolliverllc.example</div>
  </div>
</section>

<section class="sheet card-back">
  <div class="brand">
    <div class="brand-square"></div>
    <div class="brand-name">Tolliver</div>
  </div>
</section>

<section class="sheet envelope-front">
  <div class="brand">
    <div class="brand-square"></div>
    <div class="brand-text">
      <div class="brand-name">Tolliver</div>
      <div class="brand-sub">Business Services</div>
    </div>
  </div>
  <div class="contact">
    PO Box 4713 Seattle, WA 98109<br>
    www.tolliverllc.example
  </div>
</section>

<section class="sheet envelope-back">
  <svg width="464" height="335" viewBox="0 0 464 335">
    <defs>
      <linearGradient id="flapShade" x1="0" y1="0" x2="0" y2="1">
        <stop offset="0" stop-color="#3a3a3a"/>
        <stop offset="1" stop-color="#6a6a6a"/>
      </linearGradient>
    </defs>
    <polyline points="0,335 200,170 264,170 464,335" fill="none" stroke="#dcdcdc" stroke-width="1"/>
    <path d="M0 0 H464 V8 L252 128 Q232 138 212 128 L0 8 Z" fill="url(#flapShade)"/>
    <rect x="222" y="84" width="20" height="20" fill="#f0f0f0"/>
  </svg>
</section>

<aside class="package-tab"><span>Stationery Package</span></aside>

</body>
</html>
```